Chiropractic healthcare group business card

We are a Portland Oregon based chiropractic healthcare group. Looking for a new business card design. Something cutting edge, that shows off our new logo and tag line.Use either of the attached logos.Our tag line = "What could you do with no ache?"I'm open to about anything, impress me!!
Target Market(s)
Chiropractic patients - Auto injury, back pain, sports injuries, neck , shoulder, hip, knee, ankle pain.
Industry/Entity Type
Chiropractic
Contact Information for Business Card
Dr. Bram Holtvick, D.C.
Clinic name - Fernway Chiropractic
2 clinics
location #1
20418 NW Marwick Road
Suite 4
Larkhaven, OR 97480
Location #2
13529 SE Calloway Street
Portland OR 97236
Main phone line 971.555.0143
website : www.FernwayClinics.example
Tag line "What could you do with no ache?"
Colors
Designer to choose colors to be used in the design.
Requirements
Must have
- Use the logo colors -- Want the orange color to be a TRUE orange.
- Both clinic address
- phone number
- website
- personal email - b.holtvick@ReliefBeginsHere.example
- tag line - "What could you do with no ache?"

```html
<!DOCTYPE html>
<html lang="en">
<head>
<meta charset="utf-8">
<title>Fernway Chiropractic – Business Card</title>
<link rel="stylesheet" href="https://fonts.googleapis.com/css2?family=Montserrat:wght@400;500;600;700&family=Nothing+You+Could+Do&display=swap">
<style>
  :root {
    --backdrop: #262220;
    --card: #3c3c3e;
    --orange: #f7941d;
    --white: #ffffff;
    --soft-white: #e9e9e9;
  }
  * { box-sizing: border-box; margin: 0; padding: 0; }
  html, body { width: 1200px; height: 900px; overflow: hidden; }
  body {
    background: var(--backdrop);
    font-family: "Montserrat", Arial, sans-serif;
    display: flex;
    flex-direction: column;
    align-items: center;
    justify-content: center;
    gap: 40px;
  }
  .card {
    position: relative;
    width: 700px;
    height: 400px;
    background: var(--card);
    overflow: hidden;
  }

  /* Shared brand lockup */
  .brand {
    display: flex;
    align-items: center;
    gap: 16px;
    color: var(--white);
    font-weight: 600;
    text-transform: uppercase;
  }
  .brand-mark {
    flex: none;
    background: var(--orange);
  }
  .brand-words {
    display: flex;
    flex-direction: column;
    align-items: center;
    line-height: 1.15;
  }

  /* Front */
  .card-front {
    display: flex;
    flex-direction: column;
    align-items: center;
    justify-content: center;
    padding-top: 20px;
  }
  .card-front .brand-mark { width: 26px; height: 26px; }
  .card-front .brand-primary { font-size: 46px; letter-spacing: 12px; margin-right: -12px; }
  .card-front .brand-secondary { font-size: 16px; letter-spacing: 4px; margin-right: -4px; font-weight: 600; }
  .rule {
    width: 300px;
    height: 2px;
    background: var(--orange);
    margin: 26px 0 16px;
  }
  .tagline {
    font-family: "Nothing You Could Do", cursive;
    color: var(--white);
    font-size: 28px;
    transform: rotate(-2deg);
  }

  /* Back */
  .accent-band {
    position: absolute;
    inset: 0;
    width: 700px;
    height: 400px;
  }
  .card-back .brand {
    position: absolute;
    top: 36px;
    right: 46px;
  }
  .card-back .brand-mark { width: 18px; height: 18px; background: var(--white); }
  .card-back .brand-primary { font-size: 28px; letter-spacing: 7px; margin-right: -7px; }
  .card-back .brand-secondary { font-size: 11px; letter-spacing: 2.5px; margin-right: -2.5px; }
  .contact {
    position: absolute;
    left: 48px;
    top: 140px;
    color: var(--soft-white);
    font-size: 15px;
    line-height: 1.5;
  }
  .contact-name {
    font-weight: 700;
    font-size: 21px;
    color: var(--white);
  }
  .contact-rule {
    width: 260px;
    height: 2px;
    background: var(--orange);
    margin: 10px 0 14px;
  }
  .location { margin-bottom: 10px; }
  .reach { margin-top: 4px; }
</style>
</head>
<body>

  <section class="card card-front" aria-label="Card front">
    <div class="brand">
      <span class="brand-mark"></span>
      <span class="brand-words">
        <span class="brand-primary">Fernway</span>
        <span class="brand-secondary">Chiropractic</span>
      </span>
    </div>
    <div class="rule"></div>
    <p class="tagline">What could you do with no ache?</p>
  </section>

  <section class="card card-back" aria-label="Card back">
    <svg class="accent-band" viewBox="0 0 700 400" aria-hidden="true">
      <polygon points="230,0 700,0 700,250" fill="var(--orange)"/>
    </svg>
    <div class="brand">
      <span class="brand-mark"></span>
      <span class="brand-words">
        <span class="brand-primary">Fernway</span>
        <span class="brand-secondary">Chiropractic</span>
      </span>
    </div>
    <div class="contact">
      <p class="contact-name">Dr. Bram Holtvick, D.C.</p>
      <div class="contact-rule"></div>
      <p class="location">20418 NW Marwick Road, Suite 4<br>Larkhaven, OR 97480</p>
      <p class="location">13529 SE Calloway Street<br>Portland, OR 97391</p>
      <p class="reach">971.555.0143<br>www.FernwayClinics.example<br>b.holtvick@ReliefBeginsHere.example</p>
    </div>
  </section>

</body>
</html>
```